Blood bank stickers for dog and cat blood donors

We’d like to create two promotional stickers to give to clients after their pet donates blood at TORLO. These will help raise awareness and celebrate our donor pets.

One for dogs: “My dog is a blood donor hero at TORLO”
One for cats: “My cat is a blood donor hero at TORLO”

It'll need to include:

1. TORLO Blood Bank

2. Address: Unit 3/218 Karrinup Drive, Wendale, 6172

2. Phone: (08) 9387 2614

3. TORLO logo (attached)

Something people would proudly display on their car or laptop.

Target Market(s)

Pet owner community

Industry/Entity Type

Veterinary

Colors
0054AA
0677BA
7BADD7
CADEEF
E8F1F8
0094D4
00A9DD
6FCCEA
C7EBF8
E9F6FB
EB3D1F
EC4F4E
F09395
F8D3D4
FCEDEE

Requirements
Must have
• "TORLO Blood Bank" & "Unit 3/218 Karrinup Drive, Wendale, 6172" & "(08) 9387 2614"
Nice to have
• Maybe a tag line like "My Dog is a Blood Donor Hero" & "My Cat is a Blood Donor Hero"

```html
<!DOCTYPE html>
<html lang="en">
<head>
<meta charset="utf-8">
<title>TORLO Blood Bank Donor Stickers</title>
<link rel="stylesheet" href="https://fonts.googleapis.com/css2?family=Montserrat:wght@600;700;800&display=swap">
<style>
  :root {
    --ring-pink: #F7A3BA;
    --blush: #FCEDEE;
    --navy: #0054AA;
    --red: #EB3D1F;
    --drop-red: #D93A33;
    --ink: #111111;
    --teal: #0677BA;
    --paper: #FFFFFF;
  }
  * { margin: 0; padding: 0; box-sizing: border-box; }
  html, body {
    width: 1200px;
    height: 2374px;
    overflow: hidden;
    background: var(--paper);
  }
  body {
    position: relative;
    font-family: "Montserrat", Arial, sans-serif;
  }
  .sticker {
    position: absolute;
    left: 75px;
    width: 1052px;
    height: 1052px;
  }
  .sticker--dog { top: 73px; }
  .sticker--cat { top: 1237px; }
  .sticker__art {
    position: absolute;
    inset: 0;
    width: 1052px;
    height: 1052px;
  }
  .sticker__ring { fill: none; stroke: var(--ring-pink); stroke-width: 11; }
  .sticker__core { fill: var(--blush); }
  .sticker__tagline {
    fill: var(--navy);
    font-family: "Montserrat", Arial, sans-serif;
    font-weight: 800;
    font-size: 40px;
  }
  .sticker__star { fill: var(--red); font-family: "Montserrat", Arial, sans-serif; font-weight: 800; font-size: 58px; }
  .sticker__drop { fill: var(--drop-red); }
  .line {
    position: absolute;
    left: 0;
    width: 100%;
    text-align: center;
    line-height: 1;
    transform: translateY(-50%);
  }
  .brand {
    top: 315px;
    display: flex;
    justify-content: center;
    align-items: center;
    gap: 18px;
    font-size: 66px;
    font-weight: 800;
    color: var(--ink);
    letter-spacing: 0.04em;
  }
  .brand__dot {
    width: 30px;
    height: 30px;
    border-radius: 50%;
    background: var(--teal);
  }
  .title {
    top: 469px;
    font-size: 52px;
    font-weight: 700;
    color: var(--red);
    letter-spacing: 0.14em;
    padding-left: 0.14em;
  }
  .label {
    font-size: 35px;
    font-weight: 700;
    color: var(--navy);
    letter-spacing: 0.14em;
    padding-left: 0.14em;
  }
  .label--address { top: 551px; }
  .label--phone { top: 723px; }
  .detail {
    font-size: 36px;
    font-weight: 700;
    color: var(--ink);
    letter-spacing: 0.13em;
    padding-left: 0.13em;
  }
  .detail--street { top: 601px; }
  .detail--town { top: 652px; }
  .detail--phone { top: 773px; }
</style>
</head>
<body>

<section class="sticker sticker--dog">
  <svg class="sticker__art" viewBox="0 0 1052 1052" aria-hidden="false">
    <defs>
      <path id="tagline-arc-dog" d="M 93 556 A 434 434 0 1 1 959 556"/>
    </defs>
    <circle class="sticker__ring" cx="526" cy="526" r="520"/>
    <circle class="sticker__core" cx="526" cy="526" r="408"/>
    <text class="sticker__tagline">
      <textPath href="#tagline-arc-dog" textLength="1400" lengthAdjust="spacing" startOffset="12">MY DOG IS A BLOOD DONOR HERO AT TORLO</textPath>
    </text>
    <text class="sticker__star" x="73" y="604" text-anchor="middle">*</text>
    <text class="sticker__star" x="979" y="604" text-anchor="middle">*</text>
    <path class="sticker__drop" role="img" aria-label="Blood drop mascot" d="M526 947 C 516 967 500 986 500 1004 A 26 26 0 0 0 552 1004 C 552 986 536 967 526 947 Z"/>
  </svg>
  <div class="line brand"><span class="brand__dot"></span><span>TORLO</span></div>
  <div class="line title">BLOOD BANK</div>
  <div class="line label label--address">ADDRESS</div>
  <div class="line detail detail--street">Unit 3/218 Karrinup</div>
  <div class="line detail detail--town">Drive, Wendale, 6172</div>
  <div class="line label label--phone">PHONE</div>
  <div class="line detail detail--phone">(08) 9387 2614</div>
</section>

<section class="sticker sticker--cat">
  <svg class="sticker__art" viewBox="0 0 1052 1052" aria-hidden="false">
    <defs>
      <path id="tagline-arc-cat" d="M 93 556 A 434 434 0 1 1 959 556"/>
    </defs>
    <circle class="sticker__ring" cx="526" cy="526" r="520"/>
    <circle class="sticker__core" cx="526" cy="526" r="408"/>
    <text class="sticker__tagline">
      <textPath href="#tagline-arc-cat" textLength="1400" lengthAdjust="spacing" startOffset="12">MY CAT IS A BLOOD DONOR HERO AT TORLO</textPath>
    </text>
    <text class="sticker__star" x="73" y="604" text-anchor="middle">*</text>
    <text class="sticker__star" x="979" y="604" text-anchor="middle">*</text>
    <path class="sticker__drop" role="img" aria-label="Blood drop mascot" d="M526 947 C 516 967 500 986 500 1004 A 26 26 0 0 0 552 1004 C 552 986 536 967 526 947 Z"/>
  </svg>
  <div class="line brand"><span class="brand__dot"></span><span>TORLO</span></div>
  <div class="line title">BLOOD BANK</div>
  <div class="line label label--address">ADDRESS</div>
  <div class="line detail detail--street">Unit 3/218 Karrinup</div>
  <div class="line detail detail--town">Drive, Wendale, 6172</div>
  <div class="line label label--phone">PHONE</div>
  <div class="line detail detail--phone">(08) 9387 2614</div>
</section>

</body>
</html>
```